Company Business Card, for Harborveldt.com Floating homes and Marinas

To design a new great looking business card that follows some how the theme of our business and website. Harborveldt.com

I have attached our logo and a copy of our existing card (boring)

   We appreciate everyones efforts so far there are some very interesting designs. We are thinking that our company is more than just a Marina manufacturer, we build many different floating products and we would like our card to show case those products. There has been one card that has done this, and we are leaning towards that design. We prefer that our logo and company name are proportional on the card, and our mission statement be also shown. Thank you                                

                                   

 We do like your designs, on the back of the card  we want to show all 6 different product types as shown on the front of our website.

                                   

Sorry some designers have the images on the front, and that is okay as well. We just want on the card all 6 areas that we manufacture.

• Must have a new look, maybe nautical, following the theme of what our company manufactures.

Logo
Company name: Consolidated Pontoon Dockworks Group, Inc.

Website: www.HarborVeldt.com

Employee name & title

Mission statement: "Craftsmanship is the keel that carries every voyage"

Our Address: 4718 Quillan Avenue, Delta, B.C. Canada, V3K 2R7

• Colour and unique presentation,

```html
<!DOCTYPE html>
<html lang="en">
<head>
<meta charset="utf-8">
<title>HarborVeldt Business Card</title>
<link rel="stylesheet" href="https://fonts.googleapis.com/css2?family=Source+Sans+3:wght@400;600;700&display=swap">
<style>
  :root {
    --backdrop: #5b3524;
    --brand-red: #ee2025;
    --card-white: #ffffff;
    --ink: #111111;
    --body-text: #333333;
    --swoosh: #1a1a1a;
    --water-deep: #1f5f8b;
    --water-light: #7fb6d6;
  }
  * { box-sizing: border-box; margin: 0; padding: 0; }
  html, body { width: 1200px; height: 964px; overflow: hidden; }
  body {
    background: var(--backdrop);
    font-family: "Source Sans 3", "Myriad Pro", Arial, sans-serif;
    position: relative;
  }
  .card {
    position: absolute;
    width: 457px;
    height: 800px;
    overflow: hidden;
  }
  .card-front { left: 114px; top: 79px; background: var(--brand-red); }
  .card-back { left: 626px; top: 76px; background: var(--card-white); }

  .wordmark {
    position: absolute;
    left: 0; right: 0;
    display: flex;
    align-items: center;
    justify-content: center;
    gap: 14px;
    font-weight: 700;
    letter-spacing: 0.5px;
  }
  .wordmark-square { width: 22px; height: 22px; flex: none; }
  .card-front .wordmark { top: 362px; font-size: 54px; color: var(--card-white); }
  .card-front .wordmark-square { background: var(--card-white); }
  .card-back .wordmark { top: 100px; font-size: 50px; color: var(--ink); }
  .card-back .wordmark-square { background: var(--brand-red); }

  .mission {
    position: absolute;
    left: 30px; right: 30px;
    top: 662px;
    text-align: center;
    color: var(--card-white);
    font-weight: 600;
    font-size: 23px;
    line-height: 32px;
  }

  .product-grid {
    position: absolute;
    left: 41px;
    top: 196px;
    width: 375px;
    display: grid;
    grid-template-columns: repeat(3, 1fr);
    gap: 10px;
  }
  .product-tile {
    height: 85px;
    background: linear-gradient(180deg, var(--water-light), var(--water-deep));
    border-bottom: 3px solid var(--brand-red);
  }

  .contact {
    position: absolute;
    left: 0; right: 0;
    top: 408px;
    text-align: center;
    color: var(--body-text);
  }
  .contact-name { color: var(--brand-red); font-weight: 700; font-size: 25px; line-height: 30px; }
  .contact-title { font-size: 19px; line-height: 26px; }
  .contact-line {
    display: flex; align-items: center; justify-content: center; gap: 8px;
    font-size: 19px; line-height: 24px;
  }
  .contact-phone { margin-top: 30px; }
  .contact-email { margin-top: 17px; }
  .contact-web { margin-top: 17px; font-size: 20px; letter-spacing: 1.6px; }
  .contact-address { margin-top: 31px; font-size: 18px; }
  .contact-icon { width: 18px; height: 18px; flex: none; }

  .footer-band { position: absolute; left: 0; bottom: 0; width: 457px; height: 110px; }
  .footer-company {
    position: absolute;
    left: 0; right: 0; bottom: 14px;
    text-align: center;
    color: var(--card-white);
    font-size: 19px;
  }
</style>
</head>
<body>
  <section class="card card-front">
    <div class="wordmark"><span class="wordmark-square"></span>HarborVeldt</div>
    <p class="mission">Craftsmanship is the keel that<br>carries every voyage</p>
  </section>

  <section class="card card-back">
    <div class="wordmark"><span class="wordmark-square"></span>HarborVeldt</div>

    <div class="product-grid">
      <div class="product-tile" role="img" aria-label="Photo of a floating home"></div>
      <div class="product-tile" role="img" aria-label="Photo of a marina"></div>
      <div class="product-tile" role="img" aria-label="Photo of a floating boathouse"></div>
      <div class="product-tile" role="img" aria-label="Photo of a floating breakwater"></div>
      <div class="product-tile" role="img" aria-label="Photo of a floating walkway"></div>
      <div class="product-tile" role="img" aria-label="Photo of a pontoon work platform"></div>
    </div>

    <div class="contact">
      <p class="contact-name">Elias Brandvold</p>
      <p class="contact-title">Senior Project Manager</p>
      <p class="contact-line contact-phone">
        <svg class="contact-icon" viewBox="0 0 20 20" aria-hidden="true">
          <circle cx="10" cy="10" r="8.5" fill="none" stroke="#333" stroke-width="1.6"/>
          <path d="M7 5.5c-1.2 1-1 3 .6 5.3s3.6 3.4 5 3l.8-1.3-1.8-1.3-1 .7c-.8-.3-1.8-1.4-2.2-2.3l.7-1-1.2-1.9z" fill="#333"/>
        </svg>
        604.555.0187
      </p>
      <p class="contact-line contact-email">
        <svg class="contact-icon" viewBox="0 0 20 20" aria-hidden="true">
          <path d="M2 8l8-5 8 5v8H2z" fill="#333"/>
          <path d="M3.5 8.6L10 12.6l6.5-4" fill="none" stroke="#fff" stroke-width="1.4"/>
        </svg>
        elias@HarborVeldt.com
      </p>
      <p class="contact-line contact-web">www.HarborVeldt.com</p>
      <p class="contact-line contact-address">4718 Quillan Avenue, Delta, B.C. Canada, V3K 2R7</p>
    </div>

    <svg class="footer-band" viewBox="0 0 457 110" preserveAspectRatio="none" aria-hidden="true">
      <path d="M0 18 C110 38 250 50 457 24 L457 110 L0 110 Z" fill="var(--brand-red)"/>
      <path d="M0 2 C120 30 260 40 457 18 C260 33 120 26 0 13 Z" fill="var(--swoosh)"/>
    </svg>
    <p class="footer-company">Consolidated Pontoon Dockworks Group, Inc.</p>
  </section>
</body>
</html>
```